Business Card for beauty technology startup

Design Glowra Business Card for a Beauty, based on the website identity and colors (https://www.glowra-example.com).
Glowra is a beauty tech startup that gathers helpful product info for beauty lovers and consumers (such as availability on stores, price range and product reviews) for makeup products. The card design must be young, colorful but clean, and very modern.

Target Market(s)

woman, 15-35

Industry/Entity Type

Cosmetics

Contact Information for Business Card

Full Name, address, phone

Font styles to use
Other font styles liked:
• Advent Pro

Colors
e34297
86cfc6
ffffff
5c5c5c
e8e8e8
e667a6
b2b2b2

Requirements
Must have
• One full colored side with a creative design and another with card info
• Use Color palette: #95C5C5 and/or #D38AA5
• Use fonts: Advent Pro
• Use website identity: https://www.glowra-example.com
Nice to have
• If needed extra font: Roboto

```html
<!DOCTYPE html>
<html lang="en">
<head>
<meta charset="utf-8">
<title>Glowra Business Card</title>
<link rel="stylesheet" href="https://fonts.googleapis.com/css2?family=Advent+Pro:wght@200;300&family=Roboto:wght@400;500&family=Roboto+Condensed:wght@700&display=swap">
<style>
  :root {
    --rose: #b97f94;
    --paper: #f4f4f4;
    --ink: #4a4a4a;
    --wave-grey: #a9a9a9;
    --divider: #9a9a9a;
    --stage: #2e2e2e;
  }
  * { margin: 0; padding: 0; box-sizing: border-box; }
  html, body { width: 1200px; height: 960px; overflow: hidden; }
  body { background: var(--stage); position: relative; font-family: "Roboto", sans-serif; }

  .card {
    position: absolute; width: 600px; height: 342px;
    border-radius: 22px; overflow: hidden; background: var(--paper);
  }
  .card--front { left: 314px; top: 113px; }
  .card--back { left: 311px; top: 472px; background: var(--rose); }

  .card__art { position: absolute; inset: 0; width: 600px; height: 342px; }

  .brand-mark {
    position: absolute; left: 116px; top: 58px; width: 96px; height: 96px;
    border: 2px solid var(--rose); border-radius: 50%;
  }
  .wordmark {
    position: absolute; left: 40px; width: 250px; top: 186px; text-align: center;
    font-family: "Advent Pro", sans-serif; font-weight: 200; font-size: 46px;
    letter-spacing: 5px; color: var(--rose); line-height: 1;
  }
  .divider {
    position: absolute; left: 299px; top: 37px; width: 1.5px; height: 205px;
    background: linear-gradient(var(--paper), var(--divider) 20%, var(--divider) 80%, var(--paper));
  }
  .contact { position: absolute; left: 337px; top: 45px; color: var(--ink); }
  .contact__name {
    font-family: "Roboto Condensed", sans-serif; font-weight: 700; font-size: 21px;
    color: var(--rose); line-height: 1;
  }
  .contact__role { font-weight: 500; font-size: 15px; margin-top: 6px; }
  .contact__address { font-size: 14.5px; line-height: 19px; margin-top: 12px; }
  .contact__list { list-style: none; margin-top: 10px; }
  .contact__list li { display: flex; align-items: center; font-size: 14.5px; height: 19.3px; }
  .contact__list svg { width: 13px; height: 13px; margin-right: 10px; fill: var(--rose); flex: none; }

  .back__circle {
    position: absolute; left: 258px; top: -4px; width: 350px; height: 350px;
    border-radius: 50%; background: var(--paper);
  }
  .back__fill { position: absolute; left: 433px; top: 0; right: 0; bottom: 0; background: var(--paper); }
  .back__wordmark {
    position: absolute; left: 38px; top: 248px;
    font-family: "Advent Pro", sans-serif; font-weight: 200; font-size: 50px;
    letter-spacing: 5px; color: #fff; line-height: 1;
  }
  .back__url {
    position: absolute; left: 40px; top: 301px;
    font-family: "Roboto", sans-serif; font-size: 12.5px; letter-spacing: 4.2px; color: #fff;
  }
</style>
</head>
<body>

<section class="card card--front" aria-label="Card front">
  <svg class="card__art" viewBox="0 0 600 342" aria-hidden="true">
    <path d="M14,306 C110,266 230,270 340,286 C440,300 520,280 570,228 C520,290 440,312 330,302 C220,292 110,292 14,306 Z" fill="var(--wave-grey)"/>
    <path d="M0,320 C110,288 250,306 380,306 C480,306 560,262 600,190 L600,342 L0,342 Z" fill="var(--rose)"/>
    <path d="M0,314 C110,282 250,300 380,300 C480,300 556,258 596,188" fill="none" stroke="#fff" stroke-width="2.5"/>
  </svg>

  <div class="brand-mark" aria-hidden="true"></div>
  <div class="wordmark">GLOWRA</div>
  <div class="divider"></div>

  <div class="contact">
    <p class="contact__name">MARA ELLISON</p>
    <p class="contact__role">CEO/FOUNDER</p>
    <p class="contact__address">2140 Willowbend Road<br>Larkfield, Oregon 97410</p>
    <ul class="contact__list">
      <li><svg viewBox="0 0 16 16"><path d="M3 1l3 3-1.5 2c1 2 3 4 5 5l2-1.5 3 3-2 2C6 14 2 10 1 3z"/></svg>555 210 4836</li>
      <li><svg viewBox="0 0 16 16"><path d="M4 0h8a1 1 0 011 1v14a1 1 0 01-1 1H4a1 1 0 01-1-1V1a1 1 0 011-1zm1 2v10h6V2z"/></svg>555 318 7720</li>
      <li><svg viewBox="0 0 16 16"><path d="M4 1h7l2 2v4H4zM1 8h14v6H1zm3 2v2h8v-2z"/></svg>555 942 1065</li>
      <li><svg viewBox="0 0 16 16"><path d="M1 3h14v10H1zm1.5 1.5L8 9l5.5-4.5V12h-11z"/></svg>info@glowra-example.com</li>
      <li><svg viewBox="0 0 16 16"><circle cx="8" cy="8" r="7"/><path d="M4 5c2 0 3 1 2 3s1 3 2 5M10 2c-1 2 1 3 3 3" stroke="var(--paper)" stroke-width="1.3" fill="none"/></svg>www.glowra-example.com</li>
    </ul>
  </div>
</section>

<section class="card card--back" aria-label="Card back">
  <div class="back__fill" aria-hidden="true"></div>
  <div class="back__circle" aria-hidden="true"></div>
  <div class="back__wordmark">GLOWRA</div>
  <div class="back__url">www.glowra-example.com</div>
</section>

</body>
</html>
```